Law Firm Needs a new Website Design

We need a new website design for our law firm located in Manhattan (Law Offices of Tobias R. Venkland, PLLC).
We have an existing logo that we will to continue using, which can be found in www.VenklandLaw.example.
The Prime Counsel, Top Advocates Logo should also be reflected near the bottom of the Home page.
The website will be 6 pages.

Deliverables:
I want a
1) home page,
2) About Us/Practice Areas page,
3) attorneys,
4) News and Articles page, and
5) Contact and Directions/Privacy Policy page.

The colors of my logo should be in the website.
I also like a touch of black and red.

The website should project "excellence."
We seek to provide the highest quality legal services.
We handle estate planning, wills, trusts, planning for people with disabilities, asset protection and preservation, Medicaid planning, hospital safe discharge, nursing home placement, powers of attorney, health care proxies, living wills, guardianships, probate, estate administration and related litigation.

I would like the colors of my Logo used (including shading where appropriate).
I also want some black on the borders and/or bottom and some red touches throughout the page.

My Logo should appear everywhere that "Law Offices Of Tobias R. Venkland, PLLC" appears.
I want the badges for Prime counsel, Top Advocates, Top Legal Practices, and ZELQ on the Home page.
I do not want too much text on the home page.

We would also like the website to have coding.
The final design should also communicate quality, expertise and stability.
Great start so far by the people who submitted designs.
Thank you.

Industry/Entity Type

Law Firm

Coding

Coded - Design and coding required

Number of Pages Required

5+ page

Colors
3276b5
ec1f27
474747

Requirements
Must have
• Please use my logo each time you mention Law Offices of Tobias R. Venkland, PLLC. Please include the Primecounsel, Top Advocates, Top Legal Practices and Zelq rating Badges on the web home page. I only wish to be contacted by phone. I am not including testimonials and am only using the New York City address.
Nice to have
• Prefer illustrations to photos regarding practice areas
Should not have
• Testimonials, contact me by email, free consultation.

```html
<!DOCTYPE html>
<html lang="en">
<head>
<meta charset="utf-8">
<title>Law Offices of Tobias R. Venkland, PLLC</title>
<link href="https://fonts.googleapis.com/css2?family=Cinzel:wght@400;600&family=Lato:wght@400;700&display=swap" rel="stylesheet">
<style>
:root{
  --navy:#1f3f6e;
  --blue:#3276b5;
  --blue-dark:#1d4f86;
  --footer:#3a7fc3;
  --red:#ec1f27;
  --ink:#474747;
  --text:#444;
  --panel:#ececec;
  --line:#cfcfcf;
  --white:#fff;
}
*{box-sizing:border-box;margin:0;padding:0}
html,body{width:814px;height:1200px;overflow:hidden;background:var(--white)}
body{position:relative;font-family:'Lato',sans-serif;color:var(--text)}
.abs{position:absolute}

/* header */
.brand{left:88px;top:8px;display:flex;align-items:center;gap:10px}
.brand-square{width:44px;height:44px;background:var(--navy)}
.brand-name{font-family:'Cinzel',serif;font-weight:400;color:var(--navy);text-align:center;line-height:1}
.brand-name .small{display:block;font-size:12px;letter-spacing:1.5px}
.brand-name .big{display:block;font-size:23px;margin:2px 0 1px}
.header-phone{left:603px;top:5px;display:flex;align-items:center;gap:5px;font-weight:700;font-size:15px;color:#222}
.search{left:556px;top:35px;width:169px;height:23px;border:1px solid #ccc;font-size:9px;color:#777;padding:5px 7px;display:flex;justify-content:space-between}

/* nav */
.nav{left:0;top:70px;width:814px;height:31px;background:linear-gradient(#3f7fc2,#1d4f86)}
.nav ul{list-style:none;position:absolute;left:88px;top:0;display:flex;height:31px}
.nav li{font-family:'Cinzel',serif;font-size:11.5px;letter-spacing:.5px;color:var(--white);display:flex;align-items:center;justify-content:center;border-right:1px solid rgba(255,255,255,.25);height:31px}
.nav li.active{background:#3d3d3d}

/* hero */
.hero{left:0;top:101px;width:814px;height:324px;background:linear-gradient(180deg,#d6e0e7 0%,#b4c3cf 35%,#7d8b96 65%,#4d5862 100%)}
.hero-title{left:90px;top:147px;font-family:'Cinzel',serif;font-weight:600;font-size:17.5px;line-height:24px;color:#1e2a3a;letter-spacing:.6px}

/* call-back form */
.form-tab{left:89px;top:362px;width:203px;height:33px;background:var(--blue);color:var(--white);font-family:'Cinzel',serif;font-size:16px;display:flex;align-items:center;justify-content:center}
.form-box{left:89px;top:395px;width:203px;height:410px;background:var(--white);border:3px solid #2a5a93;border-top:none}
.form-intro{left:0;top:16px;width:197px;text-align:center;font-size:12.5px;line-height:18px;color:#333}
.field{left:10px;width:178px;height:25px;border:1px solid #ccc;font-size:9.5px;color:#555;padding:6px 8px}
.captcha-label{left:11px;top:260px;font-size:9px;color:#555}
.captcha-num{left:12px;top:286px;font-size:13px;color:var(--red)}
.terms{left:11px;top:318px;font-size:8.5px;line-height:12px;color:#555}
.terms u{color:#1a3ea0}
.submit{left:54px;top:360px;width:80px;height:26px;background:linear-gradient(#2d5d94,#1b426f);color:var(--white);font-weight:700;font-size:12px;display:flex;align-items:center;justify-content:center;border-radius:2px}

/* about */
.about-title{left:317px;top:439px;font-family:'Cinzel',serif;font-weight:400;font-size:14.5px;color:var(--navy)}
.about-rule{left:317px;top:463px;width:408px;height:1px;background:var(--line)}
.about-text{left:317px;top:470px;width:408px;font-size:8.8px;line-height:14px;color:var(--text)}
.about-text b{color:var(--navy)}

.panels{left:315px;top:538px;width:410px;height:267px;background:var(--panel)}
.panel-title{font-family:'Cinzel',serif;font-weight:400;font-size:14.5px;color:#1e2a3a}
.practice-list{left:10px;top:41px;list-style:none}
.practice-list li{font-size:9.2px;font-weight:700;color:#2e3a4c;height:15px;display:flex;align-items:center;gap:5px}
.practice-list li::before{content:"";width:4px;height:4px;background:#8a96a6;transform:rotate(45deg)}
.practice-list li.current{color:var(--navy)}
.news-col{left:236px;top:0;width:174px;height:267px;background:#efefef}
.news-item{left:13px;width:153px;height:57px;border-bottom:1px solid #d6d6d6;display:flex;gap:8px}
.news-item .date{width:22px;text-align:center;font-size:7px;color:#555}
.news-item h4{font-size:8.5px;color:var(--navy);font-weight:700}
.news-item p{font-size:8.3px;line-height:11px;color:#444}

/* accreditations */
.accred{left:0;top:836px;width:814px;height:96px;background:var(--panel)}
.accred-title{left:92px;top:22px;font-family:'Cinzel',serif;font-weight:400;font-size:21px;line-height:27px;color:#1e2a3a}
.badge{top:18px;width:113px;height:62px;background:var(--white);border:1px solid #9a9a9a;display:flex;align-items:center;justify-content:center}

/* office */
.map{left:0;top:958px;width:814px;height:177px;background:linear-gradient(135deg,#e8e5de,#dcd9d1)}
.office{left:0;bottom:0;width:100%;height:57px;background:rgba(55,55,55,.82);color:var(--white);padding:4px 0 0 89px}
.office h3{font-size:11.5px;font-weight:700}
.office p{font-size:10.3px;margin-top:1px}
.office .phones{display:flex;align-items:center;gap:6px;font-size:11.5px;margin-top:3px}

/* footer */
.footer{left:0;top:1135px;width:814px;height:65px;background:var(--footer);color:var(--white)}
.footer-links{left:90px;top:17px;font-size:8.8px;display:flex;gap:9px}
.copyright{left:90px;top:40px;font-size:8.8px}
.follow{left:646px;top:14px;font-size:11.5px;font-weight:700}
.social{left:645px;top:36px;display:flex;gap:3px}
.social span{width:18px;height:18px;border-radius:50%;background:var(--white)}
</style>
</head>
<body>

<header>
  <div class="abs brand" aria-label="Law Offices of Tobias R. Venkland, PLLC">
    <div class="brand-square"></div>
    <div class="brand-name"><span class="small">Law Offices of</span><span class="big">Tobias R. Venkland</span><span class="small">PLLC</span></div>
  </div>
  <div class="abs header-phone">
    <svg width="18" height="18" viewBox="0 0 18 18"><circle cx="9" cy="9" r="8" fill="none" stroke="#222" stroke-width="1.3"/><path d="M6 5.2l1.6-.4.9 2-1 .8a6 6 0 0 0 2.9 2.9l.8-1 2 .9-.4 1.6c-3.6.3-7.1-3.2-6.8-6.8z" fill="#222"/></svg>
    (212) 555-0148
  </div>
  <div class="abs search"><span>Search</span>
    <svg width="11" height="11" viewBox="0 0 11 11"><circle cx="4.5" cy="4.5" r="3.5" fill="none" stroke="#aaa" stroke-width="1.2"/><path d="M7 7l3 3" stroke="#aaa" stroke-width="1.2"/></svg>
  </div>
</header>

<nav class="abs nav">
  <ul>
    <li class="active" style="width:80px">Home</li>
    <li style="width:151px">Practice Areas</li>
    <li style="width:126px">Attorneys</li>
    <li style="width:98px">News</li>
    <li style="width:181px">Contact &amp; Directions</li>
  </ul>
</nav>

<section class="abs hero" role="img" aria-label="Photograph of the Manhattan skyline"></section>
<h1 class="abs hero-title">We care about our clients<br>and believe in cultivating<br>long-term relationships</h1>
<svg class="abs" style="left:28px;top:248px" width="16" height="28" viewBox="0 0 16 28"><path d="M14 2L3 14l11 12" fill="none" stroke="#fff" stroke-width="2"/></svg>
<svg class="abs" style="left:778px;top:248px" width="16" height="28" viewBox="0 0 16 28"><path d="M2 2l11 12L2 26" fill="none" stroke="#fff" stroke-width="2"/></svg>

<div class="abs form-tab">Request a Call Back</div>
<form class="abs form-box">
  <p class="abs form-intro">Fill out this form and we will<br>call you to discuss your matter</p>
  <svg class="abs" style="left:25px;top:60px" width="148" height="12" viewBox="0 0 148 12"><path d="M0 6h66M82 6h66" stroke="#ddd"/><path d="M74 1l5 5-5 5-5-5z" fill="#fff" stroke="#aaa"/></svg>
  <div class="abs field" style="top:82px">First Name</div>
  <div class="abs field" style="top:114px">Last Name</div>
  <div class="abs field" style="top:146px">Phone</div>
  <div class="abs field" style="top:178px">Best Time To Call</div>
  <div class="abs field" style="top:209px;height:37px">Case Details</div>
  <p class="abs captcha-label">Please type the number below :</p>
  <span class="abs captcha-num">1234</span>
  <svg class="abs" style="left:50px;top:289px" width="22" height="8" viewBox="0 0 22 8"><path d="M0 4h20M16 1l4 3-4 3" fill="none" stroke="#999"/></svg>
  <div class="abs field" style="left:76px;top:283px;width:87px">Enter Number</div>
  <p class="abs terms">By submitting this form, I agree to the<br><u>Privacy Policy</u> and <u>Terms of Use.</u></p>
  <div class="abs submit">SUBMIT</div>
</form>

<h2 class="abs about-title">About Law Offices Of Tobias R. Venkland, PLLC</h2>
<div class="abs about-rule"></div>
<p class="abs about-text">Lorem ipsum dolor sit amet, consectetuer adipiscing elit, sed diam nonummy nibh euismod tincidunt ut laoreet dolore magna aliquam erat volutpat. Ut wisi enim ad minim veniam, quis nostrud exerci tation ullamcorper suscipit lobortis nisl ut aliquip ex ea commodo consequat. Duis autem vel eum iriure dolor in hendrerit in vulputate velit esse molestie consequat, vel illum dolore...<b>[+]</b></p>

<section class="abs panels">
  <h2 class="abs panel-title" style="left:8px;top:8px">Practice Areas</h2>
  <div class="abs" style="left:8px;top:30px;width:213px;height:1px;background:var(--line)"></div>
  <ul class="abs practice-list">
    <li class="current">Estate Planning</li>
    <li>Wills</li>
    <li>Trusts</li>
    <li>Planning For People With Disabilities</li>
    <li>Asset Protection &amp; Preservation</li>
    <li>Medicaid Planning</li>
    <li>Hospital Safe Discharge</li>
    <li>Nursing Home Placement</li>
    <li>Powers Of Attorney</li>
    <li>Health Care Proxies</li>
    <li>Living Wills</li>
    <li>Guardianships</li>
    <li>Probate</li>
    <li>Estate Administration &amp; Related Litigation</li>
  </ul>
  <div class="abs news-col">
    <h2 class="abs panel-title" style="left:14px;top:8px">Recent News</h2>
    <svg class="abs" style="left:152px;top:12px" width="14" height="8" viewBox="0 0 14 8"><path d="M4 1L1 4l3 3M10 1l3 3-3 3" fill="none" stroke="#888"/></svg>
    <div class="abs" style="left:13px;top:30px;width:153px;height:1px;background:var(--line)"></div>
    <div class="abs" style="left:0;top:36px">
      <div class="abs news-item" style="top:0"><div class="date"><svg width="22" height="20" viewBox="0 0 22 20"><rect x="1" y="3" width="20" height="16" fill="#fff" stroke="#555"/><rect x="1" y="3" width="20" height="3" fill="#555"/><path d="M6 1v4M16 1v4" stroke="#555" stroke-width="1.5"/><text x="11" y="17" font-size="10" text-anchor="middle" fill="#444" font-family="Lato">13</text></svg>JULY</div><div><h4>Lorem ipsum dolor</h4><p>Lorem ipsum dolor mi sit amet consen ctetbk adip iscingh.</p></div></div>
      <div class="abs news-item" style="top:58px"><div class="date"><svg width="22" height="20" viewBox="0 0 22 20"><rect x="1" y="3" width="20" height="16" fill="#fff" stroke="#555"/><rect x="1" y="3" width="20" height="3" fill="#555"/><path d="M6 1v4M16 1v4" stroke="#555" stroke-width="1.5"/><text x="11" y="17" font-size="10" text-anchor="middle" fill="#444" font-family="Lato">13</text></svg>JULY</div><div><h4>Lorem ipsum dolor</h4><p>Lorem ipsum dolor mi sit amet consen ctetbk adip iscingh.</p></div></div>
      <div class="abs news-item" style="top:117px"><div class="date"><svg width="22" height="20" viewBox="0 0 22 20"><rect x="1" y="3" width="20" height="16" fill="#fff" stroke="#555"/><rect x="1" y="3" width="20" height="3" fill="#555"/><path d="M6 1v4M16 1v4" stroke="#555" stroke-width="1.5"/><text x="11" y="17" font-size="10" text-anchor="middle" fill="#444" font-family="Lato">13</text></svg>JULY</div><div><h4>Lorem ipsum dolor</h4><p>Lorem ipsum dolor mi sit amet consen ctetbk adip iscingh.</p></div></div>
      <div class="abs news-item" style="top:176px;border-bottom:none"><div class="date"><svg width="22" height="20" viewBox="0 0 22 20"><rect x="1" y="3" width="20" height="16" fill="#fff" stroke="#555"/><rect x="1" y="3" width="20" height="3" fill="#555"/><path d="M6 1v4M16 1v4" stroke="#555" stroke-width="1.5"/><text x="11" y="17" font-size="10" text-anchor="middle" fill="#444" font-family="Lato">13</text></svg>JULY</div><div><h4>Lorem ipsum dolor</h4><p>Lorem ipsum dolor mi sit amet consen ctetbk adip iscingh.</p></div></div>
    </div>
  </div>
</section>

<section class="abs accred">
  <h2 class="abs accred-title">Our<br>Accreditations</h2>
  <svg class="abs" style="left:278px;top:0" width="64" height="96" viewBox="0 0 64 96"><path d="M0 0h16l46 48-46 48H0l46-48z" fill="#b9cdd9"/></svg>
  <div class="abs badge" style="left:358px" aria-label="Prime Counsel badge"><div style="width:82px;height:20px;background:#c9a24a"></div></div>
  <div class="abs badge" style="left:484px" aria-label="Top Advocates badge"><div style="width:82px;height:20px;background:#2a4f93"></div></div>
  <div class="abs badge" style="left:611px" aria-label="Top Legal Practices badge"><div style="width:40px;height:44px;background:#1f3f6e;border-radius:4px"></div></div>
</section>

<section class="abs map" role="img" aria-label="Street map around the Manhattan office">
  <div class="abs office">
    <h3>Manhattan office:</h3>
    <p>218 Carrow Avenue, Suite 1406, New York, New York 10121</p>
    <div class="phones">
      <svg width="12" height="12" viewBox="0 0 12 12"><path d="M1 2.5L3 1l2 3-1.3 1a6 6 0 0 0 2.8 2.8l1-1.3 3 2-1.5 2C5 11 .5 6.5 1 2.5z" fill="#fff"/></svg>(212) 555-0148
      <svg style="margin-left:8px" width="14" height="12" viewBox="0 0 14 12"><rect x="3" y="0" width="8" height="4" fill="#fff"/><rect x="0" y="4" width="14" height="6" rx="1" fill="#fff"/><rect x="3" y="8" width="8" height="4" fill="#fff" stroke="#555" stroke-width=".6"/></svg>(212) 555-0193
    </div>
  </div>
</section>

<footer class="abs footer">
  <div class="abs footer-links"><span>•&nbsp; Home</span><span>|</span><span>•&nbsp; Practice Areas</span><span>|</span><span>•&nbsp; Attorneys</span><span>|</span><span>•&nbsp; News</span><span>|</span><span>•&nbsp; Contact &amp; Directions</span></div>
  <p class="abs copyright">Copyrights© 2009-2016 Law Offices of Tobias R. Venkland, PLLC &nbsp;|&nbsp; All rights reserved &nbsp;|&nbsp; Privacy Policy</p>
  <p class="abs follow">Follow Us On</p>
  <div class="abs social"><span></span><span></span><span></span><span></span></div>
</footer>

</body>
</html>
```